I need an amazing business card!

I am the principle in my own software company that develops vexPad and mobile applications. I require a great business card design. I've attached my corporate logo (Thanks Tomasz!).
I would like the design to integrate the logo, my name, email address and skype account:
name Brent Halloway
email brenthalloway@zelqor.com
skype brenthalloway.net
I would like the back of the card to have a "write on me area" similar to the "write on me" card on this page, row 6:
http://us.pravik.com/design-templates/business-cards/#industry=Computing%20%26%20IT
As far as the rest - it's all you!
Updates
1) Please add an example telephone number as well.
Industry/Entity Type
Software
Look and feel
Each slider illustrates characteristics of the customer's brand and the style your logo design should communicate.

```html
<!DOCTYPE html>
<html lang="en">
<head>
<meta charset="UTF-8">
<title>Zelqor Business Card</title>
<link rel="stylesheet" href="https://fonts.googleapis.com/css2?family=Exo+2:wght@400;500;600&family=Open+Sans:wght@400&display=swap">
<style>
  :root {
    --page-bg: #e4e5e7;
    --brand-green: #afc353;
    --card-white: #fbfbfb;
    --name-brown: #86552a;
    --title-gray: #3a3a3a;
    --text-dark: #2e2e2e;
    --white: #ffffff;
    --write-line: rgba(255,255,255,0.75);
  }
  html, body {
    margin: 0;
    padding: 0;
    width: 1052px;
    height: 1200px;
    overflow: hidden;
    background: var(--page-bg);
  }
  .canvas {
    position: relative;
    width: 1052px;
    height: 1200px;
  }
  .card {
    position: absolute;
    left: 76px;
    width: 900px;
    height: 514px;
    box-shadow: 0 6px 18px rgba(0,0,0,0.15);
    overflow: hidden;
  }
  .card-front { top: 56px; background: var(--brand-green); }
  .card-back  { top: 630px; background: var(--card-white); }

  .brand-mark {
    position: absolute;
    background: var(--white);
    border-radius: 30px;
  }
  .card-front .brand-mark { left: 390px; top: 60px; width: 120px; height: 120px; }
  .brand-name {
    position: absolute;
    margin: 0;
    font-family: "Exo 2", sans-serif;
    font-weight: 500;
    letter-spacing: 0.55em;
    text-transform: lowercase;
    white-space: nowrap;
  }
  .card-front .brand-name {
    left: 0; right: 0; top: 200px;
    text-align: center;
    font-size: 40px;
    color: var(--white);
    padding-left: 0.55em;
  }

  .write-area {
    position: absolute;
    left: 170px; top: 300px;
    width: 560px; height: 168px;
  }
  .write-line {
    height: 0;
    border-bottom: 2px solid var(--write-line);
    margin-bottom: 52px;
  }

  .card-back .brand-mark {
    left: 610px; top: 110px; width: 136px; height: 136px;
    background: var(--brand-green);
    border-radius: 30px;
  }
  .card-back .brand-name {
    left: 540px; width: 276px; top: 270px;
    text-align: center;
    font-size: 34px;
    color: var(--brand-green);
    padding-left: 0.55em;
  }

  .holder {
    position: absolute;
    left: 50px; top: 128px;
  }
  .holder-name {
    margin: 0;
    font-family: "Exo 2", sans-serif;
    font-weight: 500;
    font-size: 31px;
    letter-spacing: 0.04em;
    text-transform: uppercase;
    color: var(--name-brown);
  }
  .holder-title {
    margin: 4px 0 0;
    font-family: "Exo 2", sans-serif;
    font-weight: 500;
    font-size: 21px;
    letter-spacing: 0.08em;
    text-transform: uppercase;
    color: var(--title-gray);
  }
  .holder-rule {
    position: absolute;
    left: 28px; top: 214px;
    width: 420px; height: 1.5px;
    background: linear-gradient(to right, var(--brand-green) 70%, rgba(175,195,83,0));
  }

  .contact-strip {
    position: absolute;
    left: 0; top: 318px;
    width: 84px; height: 196px;
  }
  .contact-list {
    position: absolute;
    left: 104px; top: 324px;
    margin: 0; padding: 0;
    list-style: none;
    font-family: "Open Sans", sans-serif;
    font-size: 17px;
    color: var(--text-dark);
  }
  .contact-list li { height: 34px; line-height: 34px; white-space: nowrap; }
  .contact-list li.address { line-height: 22px; margin-top: 18px; height: auto; }
</style>
</head>
<body>
<div class="canvas">

  <section class="card card-front" aria-label="Card front with write-on area">
    <div class="brand-mark"></div>
    <p class="brand-name">zelqor</p>
    <div class="write-area" aria-label="Space to write notes">
      <div class="write-line"></div>
      <div class="write-line"></div>
      <div class="write-line"></div>
    </div>
  </section>

  <section class="card card-back" aria-label="Card back">
    <div class="holder">
      <h1 class="holder-name">Brent Halloway</h1>
      <p class="holder-title">General Manager</p>
    </div>
    <div class="holder-rule"></div>

    <div class="brand-mark"></div>
    <p class="brand-name">zelqor</p>

    <svg class="contact-strip" viewBox="0 0 84 196" aria-hidden="true">
      <path fill="#afc353" d="M0 0 H66 V16 L76 23 L66 30 V50 L76 57 L66 64 V84 L76 91 L66 98 V138 L76 145 L66 152 V196 H0 Z"/>
      <path fill="#fff" d="M30 15 q3 -2 5 1 l2 3 q1 2 -1 3 l-1 1 q1 3 4 5 l1 -1 q2 -2 3 0 l2 3 q1 2 -1 4 q-3 2 -7 0 q-6 -4 -8 -10 q-1 -5 1 -9z"/>
      <rect x="28" y="50" width="18" height="13" rx="1" fill="#fff"/>
      <path d="M28 51 L37 58 L46 51" stroke="#afc353" stroke-width="1.6" fill="none"/>
      <path fill="#fff" d="M29 83 h16 a3 3 0 0 1 3 3 v8 a3 3 0 0 1 -3 3 h-9 l-5 4 v-4 h-2 a3 3 0 0 1 -3 -3 v-8 a3 3 0 0 1 3 -3z"/>
      <path fill="#fff" d="M37 156 c-5 -6 -8 -10 -8 -14 a8 8 0 0 1 16 0 c0 4 -3 8 -8 14z"/>
      <circle cx="37" cy="142" r="3" fill="#afc353"/>
    </svg>

    <ul class="contact-list">
      <li>012 555 0187</li>
      <li>brenthalloway@zelqor.com</li>
      <li>brenthalloway.net</li>
      <li class="address">42 Larkfield Road, 3rd building<br>Vale St.</li>
    </ul>
  </section>

</div>
</body>
</html>
```